Sticker label design for - Over Fleet Deodorant Balm

I need a label for my 100% Natural Deodorant Balm
The brand is called "Mild Meadow Brand", and the product is called OVER FLEET Deodorant Balm.
There are two labels, one is a 5.2cm circle for the top, and 4.5cm circle for the base. The jar is amber plastic with black lid.
Width: 5.8cm
Height: 3.4cm (Lid 1.2cm, base 2,2cm)
Here is a link to what the jar looks like from one of my competitors: https://redsparrow.com.au/products/body/crest-deodorant-paste/
The product is a unisex product. Please see uploaded files for designs previously made for the brand. I'm trying to see a few more designs before finalising my choice. Feel free to use the logo at the top (Mild Meadow Brand) of either attachment if you would like. Or design your own.
Be be aware that it is meant to be Aluminium and Paraben Free, not "Parabens" Weight of product is 70g, please include this.
Label can be any colour, and printed with regular colours or event gold, silver or rose gold foil. Would a background be nice?
This is something I saw that I liked:
http://www.tolvenbalm.com
However I'm really open to what people can come up with.
For the back base-
Over Fleet deodorant balm is made from 100% natural ingredients, and works by neutralises odour and minimising wetness without the use of harmful chemicals.
www.mildmeadowbrand.com
Directions: For optimal result, apply a pea size amount of the balm to your dry armpits. Gently rub the balm into your armpits covering the entire area. Discontinue use if irritation occurs.
Ingredients: Shea Butter, Coconut oil, Sodium Bicarbonate, Arrowroot, Kaolin Clay, Vitamin E, Vegetable Glycerin, Activated Charcoal, Essential oils of Peppermint, Lavender, Mandarin, Tea tree, Geranium Rose & Cedarwood.
MADE IN AUSTRALIA
Reason: Hi,
I'm not getting many submissions, so was hoping to extend the deadline.
Skin Care Product

```html
<!DOCTYPE html>
<html lang="en">
<head>
<meta charset="utf-8">
<title>Over Fleet Deodorant Balm – Lid Label</title>
<link rel="stylesheet" href="https://fonts.googleapis.com/css2?family=Russo+One&family=Questrial&family=Open+Sans:wght@700&display=swap">
<style>
  :root {
    --canvas-bg: #ffffff;
    --label-plum: #504859;
    --label-apricot: #f9ae6b;
    --rule-amber: #e8962f;
    --tagline-white: #ffffff;
  }
  html, body {
    margin: 0;
    padding: 0;
    width: 1200px;
    height: 1200px;
    overflow: hidden;
    background: var(--canvas-bg);
  }
  .label-canvas {
    display: block;
    width: 1200px;
    height: 1200px;
  }
  .label-disc { fill: var(--label-plum); }
  .tagline-rule {
    fill: none;
    stroke: var(--rule-amber);
    stroke-width: 2.5;
  }
  .tagline-text {
    fill: var(--tagline-white);
    font-family: "Open Sans", Arial, sans-serif;
    font-weight: 700;
    font-size: 40px;
    letter-spacing: 15px;
  }
  .product-name {
    fill: var(--label-apricot);
    font-family: "Russo One", "Arial Black", sans-serif;
    font-size: 124px;
  }
  .product-type {
    fill: var(--label-apricot);
    font-family: "Questrial", Arial, sans-serif;
    font-size: 54px;
  }
  .ornament-band {
    fill: none;
    stroke: var(--label-apricot);
    stroke-width: 22;
    stroke-linecap: round;
    opacity: 0.45;
  }
</style>
</head>
<body>
<svg class="label-canvas" viewBox="0 0 1200 1200" xmlns="http://www.w3.org/2000/svg">
  <defs>
    <path id="tagline-path" d="M 262 640 A 338 338 0 0 1 938 640"/>
  </defs>

  <circle class="label-disc" cx="600" cy="600" r="498"/>

  <g class="tagline">
    <path class="tagline-rule" d="M 254 466 A 363.5 363.5 0 0 1 946 466"/>
    <path class="tagline-rule" d="M 310 471 A 314 314 0 0 1 890 471"/>
    <text class="tagline-text" text-anchor="middle">
      <textPath href="#tagline-path" startOffset="50%">mild meadow brand</textPath>
    </text>
  </g>

  <text class="product-name" x="600" y="630" text-anchor="middle" textLength="778" lengthAdjust="spacingAndGlyphs">OVER FLEET</text>
  <text class="product-type" x="600" y="708" text-anchor="middle" textLength="612" lengthAdjust="spacingAndGlyphs">DEODORANT BALM</text>

  <path class="ornament-band" role="img" aria-label="Curved row of small knot ornaments" d="M 267 745 A 374 374 0 0 0 933 745"/>
</svg>
</body>
</html>
```